Identity Card Document Design

Looking for high quality identity card designs for templates.
Please read the detailed brief document which has sample designs and loads of info.
Instant Rejections :
1 You must NOT make anything illegal - anything which looks identical to an existing document. Create an ID card design entirely from scratch. Read the document for more info.
2 The artwork *has* to be provided as per the artwork specs in the document, as a print ready PDF to our size requirements.
3 No gen AI rubbish, don't waste your time, don't waste ours.
Question : In the document, there are certain letters which spell out a specific thing - what is this word? Please submit this word with your design.

```html
<!DOCTYPE html>
<html lang="en">
<head>
<meta charset="utf-8">
<title>Identity Card Template</title>
<link rel="stylesheet" href="https://fonts.googleapis.com/css2?family=Archivo:wght@400;500;600&family=Yellowtail&display=swap">
<style>
  :root {
    --backdrop: #c0c0c0;
    --card: #ffffff;
    --card-texture: #f3f3f3;
    --ink: #111111;
    --photo-slot: #d3d3d3;
  }
  html, body {
    margin: 0;
    width: 1200px;
    height: 1200px;
    overflow: hidden;
    background: var(--backdrop);
  }
  .id-card {
    position: absolute;
    left: 110px;
    top: 278px;
    width: 980px;
    height: 645px;
    background: var(--card);
    font-family: "Archivo", Arial, sans-serif;
    color: var(--ink);
    overflow: hidden;
  }
  .card-texture {
    position: absolute;
    inset: 0;
    background: radial-gradient(circle at 50% 50%, #f7f7f7, var(--card-texture));
  }
  .field {
    position: absolute;
    left: 116px;
  }
  .field-label {
    display: block;
    font-size: 15px;
    font-weight: 500;
    letter-spacing: 0.2px;
    text-transform: uppercase;
    line-height: 1;
  }
  .field-value {
    display: block;
    margin-top: 11px;
    font-size: 26px;
    font-weight: 600;
    letter-spacing: 0.4px;
    line-height: 1;
  }
  .field-address .field-value {
    margin-top: 8px;
    font-size: 16px;
    line-height: 22px;
    letter-spacing: 0.2px;
  }
  .photo-slot {
    position: absolute;
    left: 697px;
    top: 92px;
    width: 162px;
    height: 180px;
    border-radius: 18px;
    background: var(--photo-slot);
  }
  .field-right {
    left: auto;
    right: 121px;
    text-align: right;
  }
  .field-right .field-label {
    font-size: 18px;
  }
  .card-number {
    top: 337px;
  }
  .card-number .field-value {
    font-size: 27px;
    font-weight: 500;
    letter-spacing: 0.6px;
  }
  .signature {
    top: 510px;
  }
  .signature .field-value {
    margin-top: 12px;
    font-family: "Yellowtail", cursive;
    font-size: 44px;
    font-weight: 400;
    letter-spacing: 1px;
  }
</style>
</head>
<body>
  <section class="id-card">
    <div class="card-texture" role="img" aria-label="Subtle guilloche security pattern of overlapping arcs"></div>

    <div class="field" style="top:51px"><span class="field-label">First name (s)</span><span class="field-value">MARLOWE</span></div>
    <div class="field" style="top:128px"><span class="field-label">Surname</span><span class="field-value">TRENHOLM</span></div>
    <div class="field" style="top:205px"><span class="field-label">Date of birth</span><span class="field-value">31/12/1900</span></div>
    <div class="field" style="top:282px"><span class="field-label">Place of study</span><span class="field-value">PLACEOFSTUDY</span></div>
    <div class="field" style="top:359px"><span class="field-label">Place of birth</span><span class="field-value">PLACEOFBIRTH</span></div>
    <div class="field" style="top:436px"><span class="field-label">MRZ concatenation</span><span class="field-value">&lt;MRZ&lt;AREA&lt;</span></div>
    <div class="field field-address" style="top:511px"><span class="field-label">Address</span><span class="field-value">14 ASHCOMBE LANE, FERNVALE,<br>NEW SOUTH WALES, POSTCODE,<br>AUSTRALIA</span></div>

    <div class="photo-slot" role="img" aria-label="Cardholder photo area"></div>

    <div class="field field-right card-number"><span class="field-label">Card number</span><span class="field-value">1002 3456 - 22 22 22</span></div>
    <div class="field field-right signature"><span class="field-label">Cardholder signature</span><span class="field-value">Signature</span></div>
  </section>
</body>
</html>
```